Oil and Gas Company: Letterhead Design

In short we need a professional company letterhead designed for our Oil and Gas company.

We would like to keep the design simple and professional. Letterhead to include the company logo and color scheme, front page and continuation pages.

For reference, see attached logo below with our company logo and color scheme.

Target Market(s)

Oil & Gas Market

Industry/Entity Type

Oil And Gas

Font styles to use
Sans Serif

Requirements
Must have
• Letterhead must contain a front page & continuation page.
• Must be simple and professional in design.
• Follow our logo and color scheme.
Nice to have
• I would like to have the logo embedded in the bottom right hand portion of the page to provide some depth into the letterhead.

```html
<!DOCTYPE html>
<html lang="en">
<head>
<meta charset="utf-8">
<title>Ridgeline Oilfield Services – Letterhead</title>
<link href="https://fonts.googleapis.com/css2?family=Arimo:wght@400;500&display=swap" rel="stylesheet">
<style>
  :root {
    --backdrop: #4b3324;
    --paper: #ffffff;
    --ink: #2b2b2b;
    --ink-soft: #444444;
    --brand-blue: #1b4f9c;
    --brand-red: #e02127;
    --rule: #c9c9c9;
    --caption: #ffffff;
  }
  * { box-sizing: border-box; margin: 0; padding: 0; }
  html, body { width: 1200px; height: 830px; overflow: hidden; }
  body {
    background: var(--backdrop);
    font-family: "Arimo", Arial, sans-serif;
    color: var(--ink);
    position: relative;
  }
  .sheet {
    position: absolute;
    top: 46px;
    width: 531px;
    height: 688px;
    background: var(--paper);
    box-shadow: 0 4px 14px rgba(0,0,0,0.35);
    overflow: hidden;
  }
  .sheet--front { left: 42px; }
  .sheet--continuation { left: 587px; }

  .brand-name {
    position: absolute;
    left: 14px;
    top: 70px;
    width: 84px;
    text-align: center;
    font-size: 8px;
    font-weight: 500;
    letter-spacing: 0.4px;
    line-height: 9px;
    color: var(--ink);
    text-transform: uppercase;
  }

  .address {
    position: absolute;
    left: 397px;
    top: 21px;
    height: 32px;
    border-left: 1px solid var(--rule);
    padding-left: 10px;
    display: flex;
    gap: 6px;
    font-size: 8.5px;
    line-height: 11px;
    color: var(--ink-soft);
  }
  .address svg { flex: none; margin-top: 1px; }

  .contact {
    position: absolute;
    left: 0;
    right: 0;
    top: 634px;
    font-size: 10.2px;
    color: var(--ink-soft);
    text-align: center;
  }
  .contact__row {
    display: flex;
    justify-content: center;
    align-items: center;
    line-height: 14px;
  }
  .contact__row + .contact__row { margin-top: 4px; }
  .contact__item { display: inline-flex; align-items: center; gap: 4px; }
  .contact__sep {
    width: 1px; height: 12px; background: var(--rule); margin: 0 13px;
  }
  .band { position: absolute; left: 0; bottom: 0; width: 531px; height: 12px; display: block; }

  .caption {
    position: absolute;
    font-size: 28px;
    color: var(--caption);
    font-weight: 400;
  }
  .caption--front { left: 214px; top: 756px; }
  .caption--continuation { left: 810px; top: 748px; }
</style>
</head>
<body>

<section class="sheet sheet--front" aria-label="Front page">
  <div class="brand-name">Ridgeline<br>Oilfield Services</div>

  <address class="address">
    <svg width="8" height="11" viewBox="0 0 8 11" aria-hidden="true">
      <path d="M4 0C1.8 0 0 1.7 0 3.9 0 6.6 4 11 4 11s4-4.4 4-7.1C8 1.7 6.2 0 4 0z" fill="var(--brand-red)"/>
      <circle cx="4" cy="3.9" r="1.5" fill="#fff"/>
    </svg>
    <span>Street Name, City Name<br>State Zipcode</span>
  </address>

  <div class="contact">
    <div class="contact__row">
      <span class="contact__item">
        <svg width="10" height="10" viewBox="0 0 10 10" aria-hidden="true"><circle cx="5" cy="5" r="4.3" fill="none" stroke="var(--brand-blue)" stroke-width="1"/><path d="M3.5 2.6c-.5.8-.3 2.6 1 3.9s2.4 1.5 2.8 1.1l-.9-1-.8.4C5 6.6 4 5.6 3.9 5l.5-.7z" fill="var(--brand-blue)"/></svg>
        123-456-7890
      </span>
      <span class="contact__sep"></span>
      <span class="contact__item">
        <svg width="7" height="11" viewBox="0 0 7 11" aria-hidden="true"><rect x="0.5" y="0.5" width="6" height="10" rx="1" fill="none" stroke="var(--brand-blue)"/><rect x="1.8" y="2" width="3.4" height="5" fill="var(--brand-blue)"/></svg>
        123-456-7890
      </span>
      <span class="contact__sep"></span>
      <span class="contact__item">
        <svg width="11" height="8" viewBox="0 0 11 8" aria-hidden="true"><rect width="11" height="8" fill="var(--brand-blue)"/><path d="M0 0l5.5 4.5L11 0" fill="none" stroke="#fff" stroke-width="1"/></svg>
        inquiry@ridgelineoilfield.com
      </span>
    </div>
    <div class="contact__row">
      <span class="contact__item">
        <svg width="10" height="10" viewBox="0 0 10 10" aria-hidden="true"><g fill="none" stroke="var(--brand-blue)" stroke-width="0.8"><circle cx="5" cy="5" r="4.4"/><ellipse cx="5" cy="5" rx="2" ry="4.4"/><path d="M0.6 5h8.8M1.3 2.8h7.4M1.3 7.2h7.4"/></g></svg>
        www.ridgelineoilfield.com
      </span>
    </div>
  </div>

  <svg class="band" viewBox="0 0 531 12" preserveAspectRatio="none" aria-hidden="true">
    <polygon points="0,0 255,0 230,12 0,12" fill="var(--brand-blue)"/>
    <polygon points="262,0 237,12 250,12 275,0" fill="#fff"/>
    <polygon points="266,0 531,0 531,12 241,12" fill="var(--brand-red)"/>
    <polygon points="255,0 268,0 243,12 230,12" fill="#fff"/>
  </svg>
</section>

<section class="sheet sheet--continuation" aria-label="Continuation page">
  <div class="contact">
    <div class="contact__row">
      <span class="contact__item">
        <svg width="10" height="10" viewBox="0 0 10 10" aria-hidden="true"><circle cx="5" cy="5" r="4.3" fill="none" stroke="var(--brand-blue)" stroke-width="1"/><path d="M3.5 2.6c-.5.8-.3 2.6 1 3.9s2.4 1.5 2.8 1.1l-.9-1-.8.4C5 6.6 4 5.6 3.9 5l.5-.7z" fill="var(--brand-blue)"/></svg>
        123-456-7890
      </span>
      <span class="contact__sep"></span>
      <span class="contact__item">
        <svg width="7" height="11" viewBox="0 0 7 11" aria-hidden="true"><rect x="0.5" y="0.5" width="6" height="10" rx="1" fill="none" stroke="var(--brand-blue)"/><rect x="1.8" y="2" width="3.4" height="5" fill="var(--brand-blue)"/></svg>
        123-456-7890
      </span>
      <span class="contact__sep"></span>
      <span class="contact__item">
        <svg width="11" height="8" viewBox="0 0 11 8" aria-hidden="true"><rect width="11" height="8" fill="var(--brand-blue)"/><path d="M0 0l5.5 4.5L11 0" fill="none" stroke="#fff" stroke-width="1"/></svg>
        inquiry@ridgelineoilfield.com
      </span>
    </div>
    <div class="contact__row">
      <span class="contact__item">
        <svg width="10" height="10" viewBox="0 0 10 10" aria-hidden="true"><g fill="none" stroke="var(--brand-blue)" stroke-width="0.8"><circle cx="5" cy="5" r="4.4"/><ellipse cx="5" cy="5" rx="2" ry="4.4"/><path d="M0.6 5h8.8M1.3 2.8h7.4M1.3 7.2h7.4"/></g></svg>
        www.ridgelineoilfield.com
      </span>
    </div>
  </div>

  <svg class="band" viewBox="0 0 531 12" preserveAspectRatio="none" aria-hidden="true">
    <polygon points="0,0 255,0 230,12 0,12" fill="var(--brand-blue)"/>
    <polygon points="266,0 531,0 531,12 241,12" fill="var(--brand-red)"/>
    <polygon points="255,0 268,0 243,12 230,12" fill="#fff"/>
  </svg>
</section>

<p class="caption caption--front">Page 1</p>
<p class="caption caption--continuation">Page 2</p>

</body>
</html>
```